Quorvane - corporate Business Card

We need a good look and innovative business card for a new start up company based in Los Angeles called "Quorvane". We are in a payment business, including payment card, app, and ewallet. We are expert in online payment and Card not present (CNP) transaction.
We need an innovative, modern business card.

Our logo font is Aero Matics

Target Market(s)

Startup - Bank - Online Payment - Card Manufacturing

Industry/Entity Type

Startup

Contact Information for Business Card

phone: 555 555 0173 - Address: 4270 Marbrook blvd, Alder Vale, NV 89915

Requirements
Must have
• Message: innovative, professional, expert, high tech, trust, online payment expert, security
Nice to have
• no comment
Should not have
• no Comment

```html
<!DOCTYPE html>
<html lang="en">
<head>
<meta charset="utf-8">
<title>Quorvane business card</title>
<link href="https://fonts.googleapis.com/css2?family=Exo+2:wght@400;500;600&display=swap" rel="stylesheet">
<style>
  :root {
    --backdrop: #808080;
    --card-white: #fbfbfb;
    --card-black: #0c0c0c;
    --pattern-grey: #2e2e2e;
    --brand-red: #b3121f;
    --ink: #151515;
    --card-shadow: rgba(0, 0, 0, 0.45);
  }
  * { margin: 0; padding: 0; box-sizing: border-box; }
  html, body {
    width: 1200px;
    height: 900px;
    overflow: hidden;
    background: var(--backdrop);
    font-family: "Exo 2", sans-serif;
  }
  .canvas { position: relative; width: 1200px; height: 900px; }
  .card {
    position: absolute;
    top: 270px;
    width: 457px;
    height: 283px;
    border-radius: 14px;
    box-shadow: 3px 4px 4px var(--card-shadow);
    overflow: hidden;
  }
  .card--front { left: 137px; background: var(--card-white); }
  .card--back { left: 626px; background: var(--card-black); }

  .holder { position: absolute; left: 26px; top: 28px; }
  .holder__name {
    color: var(--brand-red);
    font-size: 21px;
    font-weight: 600;
    line-height: 1.1;
  }
  .holder__role {
    color: var(--ink);
    font-size: 15px;
    font-weight: 500;
    margin-top: 1px;
  }

  .contact {
    position: absolute;
    right: 26px;
    top: 32px;
    list-style: none;
    text-align: right;
    color: var(--ink);
    font-size: 14px;
  }
  .contact__item {
    display: flex;
    align-items: center;
    justify-content: flex-end;
    gap: 7px;
    height: 21px;
  }
  .contact__icon { width: 18px; height: 18px; flex: none; }

  .brand {
    position: absolute;
    left: 104px;
    top: 104px;
    display: flex;
    align-items: center;
    gap: 9px;
  }
  .brand__dot {
    width: 76px;
    height: 76px;
    border-radius: 50%;
    background: var(--brand-red);
  }
  .brand__name {
    color: var(--brand-red);
    font-size: 41px;
    font-weight: 500;
    letter-spacing: 0.3px;
  }

  .address {
    position: absolute;
    right: 26px;
    top: 217px;
    text-align: right;
    color: var(--ink);
    font-size: 13.5px;
    font-style: normal;
    line-height: 1.4;
  }

  .back-pattern {
    position: absolute;
    inset: 0;
    background: radial-gradient(circle at 50% 50%, #222222 0%, var(--pattern-grey) 60%, #1a1a1a 100%);
  }
  .back-seal {
    position: absolute;
    left: 156px;
    top: 69px;
    width: 145px;
    height: 145px;
    border-radius: 50%;
    background: #ffffff;
  }
</style>
</head>
<body>
<main class="canvas">
  <section class="card card--front" aria-label="Business card front">
    <div class="holder">
      <p class="holder__name">Dana Whitlock</p>
      <p class="holder__role">Director</p>
    </div>
    <ul class="contact">
      <li class="contact__item">
        <span>555 555 0173</span>
        <svg class="contact__icon" viewBox="0 0 18 18" aria-hidden="true">
          <circle cx="9" cy="9" r="9" fill="#b3121f"/>
          <rect x="5.8" y="3.6" width="6.4" height="10.8" rx="1.2" fill="none" stroke="#fff" stroke-width="1.4"/>
          <circle cx="9" cy="12.3" r="0.8" fill="#fff"/>
        </svg>
      </li>
      <li class="contact__item">
        <span>www.quorvane.com</span>
        <svg class="contact__icon" viewBox="0 0 18 18" aria-hidden="true">
          <circle cx="9" cy="9" r="9" fill="#b3121f"/>
          <circle cx="9" cy="9" r="4.6" fill="none" stroke="#fff" stroke-width="1.3"/>
          <path d="M4.4 9h9.2M9 4.4c-2 2.6-2 6.6 0 9.2M9 4.4c2 2.6 2 6.6 0 9.2" fill="none" stroke="#fff" stroke-width="1"/>
        </svg>
      </li>
    </ul>
    <div class="brand">
      <span class="brand__dot" aria-hidden="true"></span>
      <span class="brand__name">quorvane</span>
    </div>
    <address class="address">4270 Marbrook blvd,<br>Alder Vale, NV 89915</address>
  </section>

  <section class="card card--back" aria-label="Business card back">
    <div class="back-pattern" role="img" aria-label="Repeating grid of small brand emblems on black"></div>
    <span class="back-seal" aria-hidden="true"></span>
  </section>
</main>
</body>
</html>
```